Facial whitening product needs a packaging design

We need a packaging design for our new product named LUMORA Ultra-Bright Serum. (btw Lumora is our brand name). We want a package to look like a high end whitening treatment and eye-kicking. Here is the dimension for the labels and the dimensions the bottle for making a box is hight 5cm width 8 cm for the label (almost around the bottle) and 9.5 cm hight and 2.7 radius for a bottle (15ml) but we think we need a big box (the example is attached for the size and pattern of the box but not for the design) but the design is not fixed and all up to the designer.

Target Market(s)

Online shopper and mass targeted but the product need to look high end.

Industry/Entity Type

Product

Font styles to use
Sans Serif

Colors
34b8a4
ffffff

Requirements
Must have
• eye-kicking box that looks high end. I think white box would be great (file attached for example) and white bottle would be great but if you come with better idea then you can change it.
Nice to have
• You should look at Vitamin c box that a attached for an inspiration
• But the design is now free-style

```html
<!DOCTYPE html>
<html lang="en">
<head>
<meta charset="utf-8">
<title>LUMORA Ultra-Bright Serum — Packaging</title>
<link rel="stylesheet" href="https://fonts.googleapis.com/css2?family=Roboto+Condensed:wght@300;400&display=swap">
<style>
  :root {
    --teal: #1a8f80;
    --teal-bright: #34b8a4;
    --teal-deep: #14786b;
    --white: #ffffff;
    --ink: #1d1d1d;
    --black-band: #0d0d0d;
    --frame: #9a9a9a;
    --cap: #eef0f0;
  }
  * { margin: 0; padding: 0; box-sizing: border-box; }
  html, body { width: 1200px; height: 659px; overflow: hidden; background: var(--white); }
  body { position: relative; font-family: "Roboto Condensed", Arial, sans-serif; }

  .bottle { position: absolute; top: 40px; height: 584px; }
  .bottle__cap {
    position: absolute; left: 0; right: 0; top: 0; height: 110px;
    border-radius: 40px 40px 4px 4px;
    background: linear-gradient(90deg, #dfe3e3 0%, var(--white) 35%, #f4f6f6 65%, #d5dada 100%);
  }
  .bottle__pump {
    position: absolute; left: 28%; right: 14%; top: 26px; height: 60px;
    border-radius: 22px 30px 4px 4px;
    background: linear-gradient(90deg, #d9dddd, var(--white) 45%, #e2e6e6);
    box-shadow: 0 1px 2px rgba(0,0,0,.08);
  }
  .bottle__body {
    position: absolute; left: 0; right: 0; top: 108px; bottom: 0;
    border-radius: 2px 2px 10px 10px; overflow: hidden;
  }
  .bottle__body::after {
    content: ""; position: absolute; inset: 0;
    background: linear-gradient(90deg, rgba(0,0,0,.14) 0%, rgba(255,255,255,.12) 30%, rgba(255,255,255,0) 55%, rgba(0,0,0,.12) 100%);
    pointer-events: none;
  }
  .volume { position: absolute; left: 0; right: 0; text-align: center; font-size: 15px; line-height: 18px; }

  /* Bottle one: banded */
  .bottle--banded { left: 67px; width: 128px; }
  .bottle--banded .bottle__body { background: var(--white); }
  .band { position: absolute; left: 0; right: 0; }
  .band--teal-top { top: 0; height: 72px; background: var(--teal); }
  .band--logo { top: 72px; height: 54px; background: var(--black-band); border-bottom: 3px solid var(--teal-bright); }
  .band--logo .brand { color: var(--white); font-size: 25px; line-height: 54px; text-align: center; font-weight: 300; letter-spacing: 1px; }
  .band--volume { top: 380px; height: 36px; background: var(--black-band); }
  .band--volume .volume { color: var(--white); top: 9px; }
  .band--teal-bottom { top: 416px; bottom: 0; background: var(--teal); }
  .bottle--banded .product-name { position: absolute; top: 236px; left: 0; right: 0; text-align: center; color: var(--teal-bright); font-size: 19px; line-height: 1.3; }

  /* Bottle two: white */
  .bottle--white { left: 224px; width: 125px; }
  .bottle--white .bottle__body { background: var(--white); }
  .vertical { position: absolute; writing-mode: vertical-rl; transform: rotate(180deg); white-space: nowrap; }
  .bottle--white .brand { left: 6px; top: 100px; font-size: 66px; font-weight: 300; color: var(--ink); letter-spacing: 2px; line-height: 1; }
  .bottle--white .product-name { left: 74px; top: 172px; font-size: 20px; color: var(--teal-bright); letter-spacing: .5px; }
  .bottle--white .volume { color: var(--ink); top: 420px; }

  /* Bottle three: teal */
  .bottle--teal { left: 384px; width: 124px; }
  .bottle--teal .bottle__body { background: var(--teal); }
  .bottle--teal .brand { left: 36px; top: 95px; font-size: 52px; font-weight: 300; color: var(--white); letter-spacing: 2px; line-height: 1; }
  .bottle--teal .product-name { position: absolute; top: 340px; left: 0; right: 0; text-align: center; color: var(--white); font-size: 19px; line-height: 1.4; }
  .bottle--teal .volume { color: var(--white); top: 420px; }

  /* Flat box label */
  .label {
    position: absolute; left: 540px; top: 83px; width: 629px; height: 508px;
    border: 1px solid var(--frame); background: var(--white);
  }
  .label__band { position: absolute; left: 0; right: 0; top: 299px; height: 81px; background: var(--teal-bright); }
  .label__brand {
    position: absolute; left: 80px; top: 312px;
    font-size: 54px; font-weight: 300; color: var(--white); letter-spacing: 4px; line-height: 1;
  }
  .label__floral {
    position: absolute; left: 400px; top: 270px; width: 168px; height: 154px;
    border-radius: 50%;
    background: radial-gradient(ellipse at 55% 55%, rgba(200,240,234,.95) 0%, rgba(120,210,196,.7) 45%, rgba(52,184,164,0) 72%);
  }
  .label__product {
    position: absolute; left: 60px; top: 402px;
    font-size: 23px; color: var(--teal-bright); letter-spacing: .5px;
  }
</style>
</head>
<body>

  <div class="bottle bottle--banded">
    <div class="bottle__cap"><div class="bottle__pump"></div></div>
    <div class="bottle__body">
      <div class="band band--teal-top"></div>
      <div class="band band--logo"><div class="brand">LUMORA</div></div>
      <div class="product-name">ULTRA-BRIGHT<br>SERUM</div>
      <div class="band band--volume"><div class="volume">150 ml</div></div>
      <div class="band band--teal-bottom"></div>
    </div>
  </div>

  <div class="bottle bottle--white">
    <div class="bottle__cap"><div class="bottle__pump"></div></div>
    <div class="bottle__body">
      <div class="vertical brand">LUMORA</div>
      <div class="vertical product-name">ULTRA-BRIGHT&nbsp; SERUM</div>
      <div class="volume">150 ml</div>
    </div>
  </div>

  <div class="bottle bottle--teal">
    <div class="bottle__cap"><div class="bottle__pump"></div></div>
    <div class="bottle__body">
      <div class="vertical brand">LUMORA</div>
      <div class="product-name">ULTRA-BRIGHT<br>SERUM</div>
      <div class="volume">150 ml</div>
    </div>
  </div>

  <div class="label">
    <div class="label__band"></div>
    <div class="label__brand">LUMORA</div>
    <div class="label__floral" role="img" aria-label="Pale teal floral illustration with leaves and petals"></div>
    <div class="label__product">ULTRA-BRIGHT SERUM</div>
  </div>

</body>
</html>
```